CalmPath Nurses' Manifesto

Design a manifesto to inspire and motivate nurses to work at minimum standards of excellence in their nursing practice.

The manifesto will become a feature of our website, at conferences, workshops and retreats. It will also be featured on other marketing tools.

Primary Market:
Nurses and/or other healthcare professionals (specifically Doctors, Occupational Therapists, Psychologists and Social Workers).

However the manifesto is equally applicable to all nurses and healthcare professionals from new graduates to very experienced senior clinicians, administration officers,managers and healthcare executive personnel.

Mainly females and primarily 35 to 65 years old, which suggests people in this target age group have extensive experience, but have become jaded'.

The purpose of our business is to assist healthcare professionals, primarily nurses, to maintain their enthusiasm and excellence in service provision, for their benefit as well as the benefit of the clients.

I have attached:
File 1: Copy Samples and examples: which has the copy for the manifesto, examples that appeal to us and our 3 attempts.
File 2: Our colour Spec Sheet, HOWEVER the colours are not necessary limited to these colours. These colours are not in the logo that will be on the manifesto. The colours on the logo attached can/or also be used.
File 3: Prototype logo. The final logo will be available within 3 to 4 days.

Requirements
Must have
• Must use the copy as per the attached file.

It should be contemporary, eye catching and motivational.

Sample 1 on the attached file (File 3: copy, samples and examples_554207 saturday, 29 june 2013 06:24:3030) Is close to what we are looking for.
Should not have
• MUST BE EASY TO READ. Each line MUST be clearly defined from each other.

```html
<!DOCTYPE html>
<html lang="en">
<head>
<meta charset="utf-8">
<title>CalmPath Nurses' Manifesto</title>
<link rel="stylesheet" href="https://fonts.googleapis.com/css2?family=Oswald:wght@500;600&family=Arimo:wght@400;700&family=Tinos:wght@400;700&family=Varela+Round&display=swap">
<style>
  :root {
    --slate: #3e5c5b;
    --leaf: #8dc63f;
    --paper: #ffffff;
    --ink: #2f4a49;
    --condensed: "Oswald", "Arial Narrow", sans-serif;
    --sans: "Arimo", Helvetica, Arial, sans-serif;
    --serif: "Tinos", "Times New Roman", serif;
    --rounded: "Varela Round", Arial, sans-serif;
  }
  html, body { margin: 0; padding: 0; overflow: hidden; background: var(--slate); }
  .manifesto {
    position: relative;
    width: 810px;
    height: 1200px;
    background: var(--slate);
    color: var(--paper);
    overflow: hidden;
  }
  .manifesto > * { position: absolute; margin: 0; line-height: 1; white-space: nowrap; }
  .sans { font-family: var(--sans); }
  .serif { font-family: var(--serif); }
  .cond { font-family: var(--condensed); font-weight: 600; text-transform: uppercase; letter-spacing: 0.5px; }
  .bold { font-weight: 700; }

  .title-tab {
    left: 147px; top: 0; width: 516px; height: 72px;
    background: var(--leaf);
    border-radius: 0 0 14px 14px;
    font-family: var(--sans); font-weight: 700; font-size: 40px;
    display: flex; align-items: center; justify-content: center;
  }
  .callout {
    background: var(--paper); color: var(--ink); border-radius: 14px;
  }
  .callout--success {
    left: 291px; top: 212px; width: 508px; height: 63px;
    display: flex; align-items: center; justify-content: center;
    font-family: var(--condensed); font-weight: 600; font-size: 31px; letter-spacing: 0.3px;
  }
  .callout--trust {
    left: 58px; top: 480px; width: 254px; height: 220px;
  }
  .callout--trust p {
    position: absolute; left: 14px; top: 14px; margin: 0;
    font-family: var(--sans); font-size: 20px; line-height: 1.3;
  }
  .callout--trust .pictogram {
    position: absolute; left: 212px; top: 88px; width: 34px; height: 112px;
    background: var(--ink); border-radius: 8px;
  }
  .brand-box {
    left: 619px; top: 1037px; width: 181px; height: 147px;
    background: var(--paper); border-radius: 14px;
    display: flex; align-items: center; justify-content: center;
    font-family: var(--sans); font-weight: 700; font-size: 30px; color: var(--ink);
  }
  .vertical-right {
    left: 756px; top: 296px; transform-origin: 0 0; transform: rotate(90deg);
    font-family: var(--sans); font-size: 24px;
  }
  .vertical-left {
    left: 12px; top: 965px; transform-origin: 0 0; transform: rotate(-90deg);
    font-family: var(--sans); font-weight: 700; font-size: 38px;
  }
  .swoosh { left: 313px; top: 626px; }
</style>
</head>
<body>
<main class="manifesto">
  <h1 class="title-tab">Nurses' Manifesto</h1>

  <p class="sans" style="left:16px;top:88px;font-size:24px;">Nurse with open</p>
  <p class="sans" style="left:288px;top:80px;font-size:39px;">hands, hearts and minds.</p>
  <p class="sans" style="left:16px;top:126px;font-size:24px;"><span class="cond">Delight</span> your clients and</p>
  <p class="sans" style="left:28px;top:156px;font-size:24px;">their expectations.</p>
  <p class="cond" style="left:332px;top:138px;font-size:45px;">Colleagues</p>
  <p class="sans" style="left:596px;top:150px;font-size:24px;">by exceeding</p>

  <p class="serif" style="left:16px;top:194px;font-size:28px;">If there is no one left</p>
  <p class="serif" style="left:16px;top:226px;font-size:28px;">to <span class="cond">Follow</span>, then lead!</p>

  <p class="callout callout--success">SEEK SUCCESS FIRSTLY FROM WITHIN</p>

  <p class="sans" style="left:14px;top:308px;font-size:68px;">Support</p>
  <p class="sans" style="left:16px;top:384px;font-size:27px;">your colleagues and</p>
  <p class="sans" style="left:16px;top:425px;font-size:27px;"><span class="cond">Champion</span> their purpose.</p>

  <p class="sans" style="left:342px;top:297px;font-size:26px;">Celebrate, respect and value the</p>
  <p class="sans" style="left:340px;top:323px;font-size:64px;">diversity of</p>
  <p class="sans" style="left:348px;top:398px;font-size:27px;"><span class="cond" style="font-size:48px;">Australian</span> culture.</p>
  <p class="sans" style="left:348px;top:458px;font-size:46px;">Smile and infect</p>
  <p class="sans" style="left:348px;top:512px;font-size:46px;">others with your</p>
  <p class="sans" style="left:348px;top:572px;font-size:27px;"><span class="cond" style="font-size:50px;">Happiness</span> and have</p>
  <p class="sans" style="left:552px;top:624px;font-size:80px;">fun!</p>

  <p class="vertical-right"><span class="cond" style="font-size:24px;">Always</span> be solution focused.</p>
  <p class="vertical-left">Be a lifelong learner</p>

  <div class="callout callout--trust">
    <p>Trust your<br>knowledge and<br>seek advice only<br>from<br>respected<br>sources.</p>
    <div class="pictogram" role="img" aria-label="Small pictogram of a nurse"></div>
  </div>

  <svg class="swoosh" width="227" height="40" viewBox="0 0 227 40" aria-hidden="true">
    <path d="M0 8 L40 0 L34 8 L227 24 L34 14 L40 36 Z" fill="var(--paper)"/>
  </svg>

  <p class="cond" style="left:64px;top:708px;font-size:60px;letter-spacing:5px;">Be a life long learner.</p>

  <p class="serif" style="left:275px;top:774px;font-size:29px;">Respect the limits of people’s</p>
  <p class="serif" style="left:275px;top:804px;font-size:29px;">knowledge and <span class="bold">share</span> your</p>
  <p class="serif" style="left:275px;top:834px;font-size:29px;">knowledge generously</p>

  <p class="serif" style="left:64px;top:816px;font-size:40px;">You are</p>
  <p class="cond" style="left:66px;top:862px;font-size:32px;">Unique, revel in</p>
  <p class="cond" style="left:66px;top:902px;font-size:30px;">Your</p>
  <p class="sans bold" style="left:64px;top:932px;font-size:45px;">individuality.</p>

  <p class="cond" style="left:361px;top:880px;font-size:50px;">Seek success</p>
  <p class="sans" style="left:361px;top:946px;font-size:42px;">firstly <span class="cond" style="font-size:44px;">From within</span></p>

  <p class="serif" style="left:12px;top:1004px;font-size:78px;">Deliver</p>
  <p style="left:14px;top:1066px;font-size:82px;font-family:var(--rounded);">care</p>
  <p class="cond" style="left:14px;top:1138px;font-size:52px;">Skillfully.</p>

  <p class="serif" style="left:296px;top:1002px;font-size:30px;">Adopt a ‘can do’</p>
  <p class="cond" style="left:296px;top:1048px;font-size:24px;">Attitude to everything</p>
  <p class="cond" style="left:296px;top:1078px;font-size:24px;">That comes</p>
  <p class="cond" style="left:296px;top:1112px;font-size:62px;">Your way</p>

  <p class="brand-box">CalmPath</p>
</main>
</body>
</html>
```